regPersonal Trainer Flyer Design

Reason: I have been very busy with other work and would like to extend the deadline to offer designers the chance to edit and improve designs with my help. Thank you for all the designs that have been sent so far.

```html
<!DOCTYPE html>
<html lang="en">
<head>
<meta charset="utf-8">
<title>Personal Trainer Flyer</title>
<link rel="stylesheet" href="https://fonts.googleapis.com/css2?family=Barlow:wght@400;500;600;700&family=Delius&display=swap">
<style>
  :root {
    --brand-blue: #1877bd;
    --ink: #111111;
    --paper: #f2f2f2;
    --page-bg: #e6e6e6;
    --white: #ffffff;
    --photo-tone-a: #8a8f96;
    --photo-tone-b: #c9b9ae;
  }
  * { box-sizing: border-box; margin: 0; padding: 0; }
  html, body { width: 1200px; height: 1000px; overflow: hidden; }
  body { background: var(--page-bg); font-family: "Barlow", Arial, sans-serif; position: relative; }

  .flyer {
    position: absolute; left: 40px; top: 104px;
    width: 1120px; height: 792px;
    background: var(--paper);
    overflow: hidden;
    box-shadow: 0 6px 18px rgba(0,0,0,0.18);
  }

  .header-blob { position: absolute; left: 0; top: 40px; width: 120px; height: 120px; }
  .trainer-portrait {
    position: absolute; left: 58px; top: 17px; width: 180px; height: 180px;
    border-radius: 50%;
    border: 5px solid var(--brand-blue);
    background: linear-gradient(135deg, var(--photo-tone-a), #4a4e55);
  }
  .trainer-name-top {
    position: absolute; left: 267px; top: 42px;
    font-size: 42px; font-weight: 400; color: var(--brand-blue); letter-spacing: 0.5px;
  }
  .header-phone {
    position: absolute; left: 729px; top: 42px;
    display: flex; align-items: center; gap: 16px;
    font-size: 44px; font-weight: 600; color: var(--brand-blue); letter-spacing: 1px;
  }
  .header-phone svg { width: 40px; height: 40px; }
  .headline {
    position: absolute; left: 265px; top: 100px;
    font-size: 76px; font-weight: 700; color: var(--brand-blue); letter-spacing: 0.5px;
  }

  .brush-band { position: absolute; left: 0; top: 220px; width: 1120px; height: 190px; }
  .pain-point {
    position: absolute; font-family: "Delius", "Comic Sans MS", cursive;
    font-size: 33px; color: var(--white); transform: rotate(-4deg); transform-origin: left bottom;
    white-space: nowrap;
  }
  .pain-point.motivation { left: 35px; top: 276px; }
  .pain-point.goals { left: 335px; top: 300px; }
  .pain-point.boredom { left: 710px; top: 318px; }

  .offer-badge {
    position: absolute; left: 862px; top: 360px; width: 206px; height: 206px;
    border-radius: 50%; background: var(--brand-blue);
    border: 6px solid var(--white);
    box-shadow: 0 3px 8px rgba(0,0,0,0.25);
    color: var(--white); text-align: center;
    display: flex; flex-direction: column; align-items: center;
    padding-top: 8px;
  }
  .offer-number { font-family: Georgia, "Times New Roman", serif; font-weight: 700; font-size: 80px; line-height: 0.9; }
  .offer-title {
    font-size: 22px; font-weight: 700; white-space: nowrap; line-height: 1.15;
    margin-top: 4px; padding: 0 4px 4px; border-bottom: 2px solid var(--white);
  }
  .offer-note { font-size: 17px; font-weight: 600; line-height: 1.2; margin-top: 5px; white-space: nowrap; }

  .help-heading {
    position: absolute; left: 24px; top: 462px;
    font-family: "Delius", "Comic Sans MS", cursive; font-weight: 700;
    font-size: 66px; color: var(--brand-blue);
  }

  .benefits-panel {
    position: absolute; left: 0; top: 578px; width: 797px; height: 214px;
    background: var(--brand-blue); border-top-right-radius: 14px;
  }
  .benefits-list { position: absolute; left: 26px; top: 28px; list-style: none; }
  .benefits-list li {
    display: flex; align-items: center; gap: 10px;
    font-size: 27px; font-weight: 500; color: var(--white); height: 54px;
  }
  .benefits-list svg { width: 26px; height: 26px; }

  .session-photo {
    position: absolute; left: 490px; top: 440px; width: 276px; height: 186px;
    border: 4px solid var(--white); border-radius: 6px;
    background: linear-gradient(120deg, #d8d2cc, var(--photo-tone-b) 45%, #5d636c);
    box-shadow: 0 2px 6px rgba(0,0,0,0.2);
  }

  .trainer-mark {
    position: absolute; left: 902px; top: 568px; width: 34px; height: 54px;
    background: var(--brand-blue); border-radius: 4px;
  }
  .contact-block { position: absolute; left: 819px; top: 622px; color: var(--brand-blue); }
  .contact-role { font-size: 25px; font-weight: 400; }
  .contact-name { font-size: 25px; font-weight: 700; margin-top: 2px; }
  .contact-line { display: flex; align-items: center; gap: 6px; font-size: 19px; margin-top: 4px; }
  .contact-line:first-of-type { margin-top: 24px; }
  .contact-line svg { width: 17px; height: 17px; }
</style>
</head>
<body>
  <div class="flyer">
    <svg class="header-blob" viewBox="0 0 120 120" aria-hidden="true">
      <path d="M0 10 C30 0 70 4 110 20 L120 110 C80 116 40 112 0 104 Z" fill="var(--brand-blue)"/>
    </svg>
    <div class="trainer-portrait" role="img" aria-label="Photo of the trainer working out on gym equipment"></div>

    <div class="trainer-name-top">Sam Keller</div>
    <div class="header-phone">
      <svg viewBox="0 0 40 40" aria-hidden="true">
        <rect width="40" height="40" rx="6" fill="var(--brand-blue)"/>
        <path d="M13 9c1 0 2 .5 2.5 1.5l2 4c.4.9.2 1.9-.5 2.5l-1.8 1.5c1.3 2.8 3.5 5 6.3 6.3l1.5-1.8c.6-.7 1.6-.9 2.5-.5l4 2c1 .5 1.5 1.5 1.5 2.5v3c0 1.4-1.1 2.5-2.5 2.5C16.5 32.5 7.5 23.5 7.5 11.5 7.5 10.1 8.6 9 10 9z" fill="var(--white)"/>
      </svg>
      <span>07700900481</span>
    </div>
    <h1 class="headline">Your Personal Trainer</h1>

    <svg class="brush-band" viewBox="0 0 1120 190" preserveAspectRatio="none" aria-hidden="true">
      <path d="M0 0 L20 12 L60 4 L90 10 L140 2 L190 14 L215 6 L260 0 L1120 0 L1120 130 L1100 150 L1080 138 L1040 160 L1000 150 L980 172 L940 160 L900 176 L870 168 L840 180 L760 176 L740 184 L600 178 L480 182 L300 176 L200 182 L120 176 L60 180 L20 172 L0 176 Z" fill="var(--ink)"/>
      <path d="M1080 140 L1120 140 L1120 160 L1100 166 Z M760 180 L820 184 L790 190 Z" fill="var(--ink)"/>
    </svg>
    <div class="pain-point motivation">Lacking motivation?</div>
    <div class="pain-point goals">Not achieving your goals?</div>
    <div class="pain-point boredom">Bored of the gym?</div>

    <div class="offer-badge">
      <div class="offer-number">1</div>
      <div class="offer-title">FREE SESSION</div>
      <div class="offer-note">Introductory<br>Offer!</div>
    </div>

    <div class="help-heading">Need help???</div>

    <div class="benefits-panel">
      <ul class="benefits-list">
        <li><svg viewBox="0 0 26 26" aria-hidden="true"><circle cx="13" cy="13" r="12" fill="var(--white)"/><path d="M7 13.5l4 4 8-8" stroke="var(--brand-blue)" stroke-width="3" fill="none" stroke-linecap="round" stroke-linejoin="round"/></svg>You‘re never too old</li>
        <li><svg viewBox="0 0 26 26" aria-hidden="true"><circle cx="13" cy="13" r="12" fill="var(--white)"/><path d="M7 13.5l4 4 8-8" stroke="var(--brand-blue)" stroke-width="3" fill="none" stroke-linecap="round" stroke-linejoin="round"/></svg>I can help improve your health and well-being</li>
        <li><svg viewBox="0 0 26 26" aria-hidden="true"><circle cx="13" cy="13" r="12" fill="var(--white)"/><path d="M7 13.5l4 4 8-8" stroke="var(--brand-blue)" stroke-width="3" fill="none" stroke-linecap="round" stroke-linejoin="round"/></svg>Training can be at your home</li>
      </ul>
    </div>

    <div class="session-photo" role="img" aria-label="Photo of the trainer coaching a client through a barbell squat in a gym"></div>

    <div class="trainer-mark" role="img" aria-label="Small figure of an athlete lifting"></div>
    <div class="contact-block">
      <div class="contact-role">Personal Trainer</div>
      <div class="contact-name">Sam Keller</div>
      <div class="contact-line">
        <svg viewBox="0 0 40 40" aria-hidden="true"><rect width="40" height="40" rx="6" fill="var(--brand-blue)"/><path d="M13 9c1 0 2 .5 2.5 1.5l2 4c.4.9.2 1.9-.5 2.5l-1.8 1.5c1.3 2.8 3.5 5 6.3 6.3l1.5-1.8c.6-.7 1.6-.9 2.5-.5l4 2c1 .5 1.5 1.5 1.5 2.5v3c0 1.4-1.1 2.5-2.5 2.5C16.5 32.5 7.5 23.5 7.5 11.5 7.5 10.1 8.6 9 10 9z" fill="var(--white)"/></svg>
        <span>07700900481</span>
      </div>
      <div class="contact-line">
        <svg viewBox="0 0 20 16" aria-hidden="true"><rect x="0" y="1" width="20" height="14" rx="1.5" fill="var(--brand-blue)"/><path d="M1 2.5l9 6.5 9-6.5" stroke="var(--white)" stroke-width="1.6" fill="none"/></svg>
        <span>samkeller@mailbox.co.uk</span>
      </div>
    </div>
  </div>
</body>
</html>
```